logo and label design for a vegan skincare Called Leafmerelle

We need a logo and label design for a skincare brand called leafmerelle based in Australia. The products are 100% natural, Australian made, small batch, vegan, cruelty-free, ethical and sustainable beauty products. The secret of our skin care products are their naturally active ingredients.
They are potent, yet incredibly gentle on sensitive skin. We believe in investing in only the highest quality and ethical ingredients to ensure we are creating products we can stand behind.
Our products use: Naturally delivered ingredients; Organic ingredients where is possible; Australian oils, fruits & Extracts; Aromatherapy oils; sustainable & ethical ingredients; natural preservatives.
Our products don't use: sulphates; parabens; phthalates; Petrochemicals; synthetic colours; synthetic fragrances. All label must be design for an amber bottle.
Label Requirements:
* 300 DPI minimum
* All fonts have been outlined
* 3mm Bleed included in artwork
Colors
Designer to choose colors to be used in the design.
Look and feel
Each slider illustrates characteristics of the customer's brand and the style your logo design should communicate.

```html
<!DOCTYPE html>
<html lang="en">
<head>
<meta charset="utf-8">
<title>Leafmerelle – Label, Logo and Product</title>
<link href="https://fonts.googleapis.com/css2?family=Titillium+Web:wght@300;400&family=Oswald:wght@700&display=swap" rel="stylesheet">
<style>
  :root {
    --board-top: #f0f0f0;
    --board-logo: #e0e0e0;
    --board-product: #ebebea;
    --paper: #ffffff;
    --ink: #111111;
    --rule: #8c8c8c;
    --leaf-light: #a3b487;
    --leaf-dark: #6f8656;
  }
  * { margin: 0; padding: 0; box-sizing: border-box; }
  html, body { width: 1200px; height: 1200px; overflow: hidden; }
  body {
    position: relative;
    font-family: "Titillium Web", sans-serif;
    color: var(--ink);
    background: var(--board-top);
  }
  .panel { position: absolute; overflow: hidden; }
  .panel-label { left: 0; top: 0; width: 1200px; height: 600px; background: var(--board-top); }
  .panel-logo { left: 0; top: 600px; width: 600px; height: 600px; background: var(--board-logo); }
  .panel-product { left: 600px; top: 600px; width: 600px; height: 600px; background: var(--board-product); }
  .panel-title {
    position: absolute; left: 29px; top: 36px;
    font-size: 26px; font-weight: 300; letter-spacing: 0.02em;
  }
  .panel-product .panel-title { left: 26px; }

  /* Label card */
  .label-card {
    position: absolute; width: 571px; height: 400px;
    background: var(--paper); overflow: hidden;
  }
  .panel-label .label-card { left: 314px; top: 106px; }
  .panel-product .label-card {
    left: 157px; top: 200px;
    transform: scale(0.5); transform-origin: top left;
    box-shadow: 0 2px 10px rgba(0,0,0,0.08);
  }
  .leaf-art {
    position: absolute;
    background: linear-gradient(135deg, var(--leaf-light), var(--leaf-dark));
    opacity: 0.85;
  }
  .leaf-top-left { left: 0; top: 0; width: 124px; height: 140px; border-radius: 0 0 100% 0; }
  .leaf-top-right { right: 0; top: 0; width: 104px; height: 80px; border-radius: 0 0 0 100%; }
  .leaf-bottom-right { right: 0; bottom: 0; width: 109px; height: 183px; border-radius: 100% 0 0 0; }
  .leaf-bottom-left { left: 0; bottom: 0; width: 49px; height: 71px; border-radius: 0 100% 0 0; }

  .brand-seal {
    position: absolute; left: 231px; top: 24px; width: 113px; height: 113px;
    border: 1px solid var(--ink); border-radius: 50%;
    display: flex; align-items: center; justify-content: center;
    font-size: 11px; font-weight: 400; letter-spacing: 0.16em;
  }
  .label-rule {
    position: absolute; left: 43px; top: 154px; width: 486px;
    border-top: 1px solid var(--rule);
  }
  .product-name {
    position: absolute; left: 43px; top: 160px;
    font-family: "Oswald", sans-serif; font-weight: 700;
    font-size: 30px; letter-spacing: 0.14em; line-height: 40px;
  }
  .label-copy {
    position: absolute; left: 43px; width: 440px;
    font-size: 8.8px; line-height: 11.3px; font-weight: 400;
  }
  .copy-directions { top: 210px; }
  .copy-ingredients { top: 244px; }
  .copy-storage { top: 322px; }
  .net-volume {
    position: absolute; left: 43px; top: 362px;
    font-size: 14.5px; font-weight: 400;
  }

  /* Logo panel */
  .logo-seal {
    position: absolute; left: 92px; top: 104px; width: 416px; height: 416px;
    border: 4px solid var(--ink); border-radius: 50%;
    display: flex; align-items: center; justify-content: center;
    font-size: 34px; font-weight: 300; letter-spacing: 0.16em;
  }
</style>
</head>
<body>

<section class="panel panel-label">
  <h2 class="panel-title">Label</h2>
  <div class="label-card">
    <div class="leaf-art leaf-top-left" role="img" aria-label="Green palm frond illustration"></div>
    <div class="leaf-art leaf-top-right" role="img" aria-label="Green palm frond illustration"></div>
    <div class="leaf-art leaf-bottom-right" role="img" aria-label="Green palm frond illustration"></div>
    <div class="leaf-art leaf-bottom-left" role="img" aria-label="Green palm frond illustration"></div>
    <div class="brand-seal">LEAFMERELLE</div>
    <div class="label-rule"></div>
    <h1 class="product-name">Purifying Gel Cleanser</h1>
    <p class="label-copy copy-directions">Directions: Gently massage in circular motions onto damp skin, avoiding eye area. Rinse away with warm water or face cloth. Follow with your favourite moisturiser. Use morning and night.</p>
    <p class="label-copy copy-ingredients">Ingredients: Purified Water, Lauryl Glucoside (Coconut &amp; Sugar Derived), Glycerin*, Cocamido Propyl Betaine (Coconut Derived), Triticum Aestivum Leaf Extract (Wheatgrass), Camellia Sinensis Leaf Extract (Green Tea), Chlorophyll (Alfalfa Grass), Citrus Sinensis (Orange) Oil, Carum Petroselinum Herb Extract (Parsley Seed), Myroxylon Pereirae (Peru Balsam) Oil, Leptospermum Petersonii (Lemon Tea Tree) Oil, Citrus Aurantium Var Amara (Petitgrain) Oil, Tocopherol (Vitamin E), Citric Acid, Hydroxymethylglycinate (Glycine Derived) - * Organic Ingredients</p>
    <p class="label-copy copy-storage">Store in a cool dry place<br>Caution For external use only. Avoid contact with eyes. If irritation occurs, discontinue use.</p>
    <p class="net-volume">200ml ℮</p>
  </div>
</section>

<section class="panel panel-logo">
  <h2 class="panel-title">Logo</h2>
  <div class="logo-seal">LEAFMERELLE</div>
</section>

<section class="panel panel-product">
  <h2 class="panel-title">Product</h2>
  <div class="label-card">
    <div class="leaf-art leaf-top-left" role="img" aria-label="Green palm frond illustration"></div>
    <div class="leaf-art leaf-top-right" role="img" aria-label="Green palm frond illustration"></div>
    <div class="leaf-art leaf-bottom-right" role="img" aria-label="Green palm frond illustration"></div>
    <div class="leaf-art leaf-bottom-left" role="img" aria-label="Green palm frond illustration"></div>
    <div class="brand-seal">LEAFMERELLE</div>
    <div class="label-rule"></div>
    <h1 class="product-name">Purifying Gel Cleanser</h1>
    <p class="label-copy copy-directions">Directions: Gently massage in circular motions onto damp skin, avoiding eye area. Rinse away with warm water or face cloth. Follow with your favourite moisturiser. Use morning and night.</p>
    <p class="label-copy copy-ingredients">Ingredients: Purified Water, Lauryl Glucoside (Coconut &amp; Sugar Derived), Glycerin*, Cocamido Propyl Betaine (Coconut Derived), Triticum Aestivum Leaf Extract (Wheatgrass), Camellia Sinensis Leaf Extract (Green Tea), Chlorophyll (Alfalfa Grass), Citrus Sinensis (Orange) Oil, Carum Petroselinum Herb Extract (Parsley Seed), Myroxylon Pereirae (Peru Balsam) Oil, Leptospermum Petersonii (Lemon Tea Tree) Oil, Citrus Aurantium Var Amara (Petitgrain) Oil, Tocopherol (Vitamin E), Citric Acid, Hydroxymethylglycinate (Glycine Derived) - * Organic Ingredients</p>
    <p class="label-copy copy-storage">Store in a cool dry place<br>Caution For external use only. Avoid contact with eyes. If irritation occurs, discontinue use.</p>
    <p class="net-volume">200ml ℮</p>
  </div>
</section>

</body>
</html>
```